Dusk n Shine - Contact/Landing Page

I need a landing page which will essentially be the page that customers will go to from the 'website' link on ZVX listing. It will provide a short overview of services which need to be selectable. a little further down can capture some contact details followed by a large Submit Now button etc...

I have some icon/logo's that can be utilised at the bottom of the page as industry type references.

End of Lease Cleaning Services

Cleaning Service

• As per description
• Colours to match my website dusknshine.com.au

```html
<!DOCTYPE html>
<html lang="en">
<head>
<meta charset="utf-8">
<title>Dusk n Shine – Cleaning Service &amp; Pest Controllers</title>
<link href="https://fonts.googleapis.com/css2?family=Poppins:wght@300;400;500;600;700&display=swap" rel="stylesheet">
<style>
:root{
  --blue:#1d86d6;
  --blue-bright:#2bb3ef;
  --navy:#14223d;
  --ink:#2b2b2b;
  --muted:#6b6f76;
  --line:#d9dde3;
  --bg:#ffffff;
  --soft:#f4f5f7;
}
*{box-sizing:border-box;margin:0;padding:0}
html,body{width:1200px;height:2836px;overflow:hidden;background:var(--bg);font-family:'Poppins',sans-serif;color:var(--ink)}
.page{position:relative;width:1200px;height:2836px;overflow:hidden}
.abs{position:absolute}

/* header */
.hero-photo{left:0;top:0;width:1200px;height:640px;background:linear-gradient(100deg,#e9ebee 0%,#f7f6f4 35%,#d9cfc4 62%,#eeeae6 80%,#c9d4cf 100%)}
.hero-curve{left:0;top:520px;width:1200px;height:200px}
.brand{left:150px;top:8px;width:90px;text-align:center}
.brand-mark{width:54px;height:54px;margin:0 auto 4px;background:var(--blue);border-radius:4px}
.brand-name{font-weight:700;font-size:18px;line-height:1.05;color:var(--blue)}
.call{left:682px;top:24px;display:flex;align-items:center;gap:10px}
.call small{display:block;font-size:13px;color:var(--ink)}
.call strong{display:block;font-size:15px;font-weight:600;color:var(--blue)}
.btn{display:inline-block;border-radius:30px;background:var(--blue-bright);color:#fff;font-weight:600;text-align:center}
.btn-quote{left:912px;top:26px;width:112px;height:34px;line-height:34px;font-size:12px;border-radius:18px}
.nav{left:450px;top:92px;display:flex;gap:26px;font-size:13px;font-weight:500}
.nav a{color:var(--ink);text-decoration:none}
.nav a.active{color:var(--blue);border-bottom:2px solid var(--blue);padding-bottom:4px}
.hero-title{left:162px;top:226px;font-size:44px;line-height:1.05;font-weight:700;color:var(--blue-bright);text-transform:uppercase}
.hero-title .amp{color:#fff}
.hero-title .small{font-size:36px}
.btn-book{left:162px;top:414px;width:168px;height:44px;line-height:44px;font-size:15px}

/* services */
.sq{width:52px;height:52px}
.sq1{left:488px;top:764px;background:var(--blue)}
.sq2{left:552px;top:764px;background:var(--blue-bright)}
.services-title{left:0;width:1200px;top:798px;text-align:center;font-size:40px;font-weight:400;color:var(--ink)}
.services-title b{font-weight:700}
.card{background:#fff;box-shadow:0 6px 26px rgba(0,0,0,.12);text-align:center;padding:28px 26px}
.card h3{font-size:15px;font-weight:700;color:var(--blue);margin:14px 0 10px;text-transform:uppercase}
.card p{font-size:11px;line-height:1.55;color:var(--muted)}
.icon-circle{width:76px;height:76px;border-radius:50%;background:var(--blue);margin:0 auto;display:flex;align-items:center;justify-content:center}
.btn-learn{display:inline-block;margin-top:18px;width:100px;height:30px;line-height:28px;border:1.5px solid var(--blue);border-radius:16px;font-size:10px;font-weight:600;color:var(--blue)}
.card-left{left:104px;top:920px;width:316px;height:280px}
.card-right{left:780px;top:920px;width:316px;height:280px}
.card-mid{left:446px;top:880px;width:312px;height:350px;background:linear-gradient(180deg,#3c5670 0%,#2f4a66 45%,#4a6d8c 100%);color:#fff;padding-top:48px}
.card-mid h3{color:#fff}
.card-mid p{color:#e8eef5}
.card-mid .icon-circle{background:transparent;border:2px solid #fff}
.card-mid .btn-learn{background:var(--blue-bright);border-color:var(--blue-bright);color:#fff}

/* contact band */
.band{left:0;top:1340px;width:1200px;height:700px}
.band-photo{left:0;top:1380px;width:1200px;height:600px;background:linear-gradient(135deg,#18253d 0%,#24354f 45%,#1a2a44 70%,#101a2c 100%)}
.email{left:232px;top:1640px;font-size:22px;color:#fff;font-weight:400}
.btn-submit{left:254px;top:1718px;width:246px;height:66px;line-height:66px;font-size:26px;border-radius:34px}
.form{left:660px;top:1612px;width:364px;height:318px;background:#fff;padding:30px 56px}
.field{height:36px;border:1px solid var(--line);font-size:11px;color:var(--blue);padding:0 12px;line-height:34px;margin-bottom:16px}
.field.grey{color:var(--muted)}
.btn-sign{display:block;height:36px;line-height:36px;background:var(--blue);color:#fff;font-size:11px;font-weight:600;text-align:center;margin-top:6px}

/* partners */
.badge{top:2176px;height:100px}
.badge1{left:150px;width:320px;background:#c6cfe0;border-radius:4px}
.badge2{left:526px;width:100px;height:100px;border-radius:50%;background:#1d6f8c}
.badge2b{left:636px;top:2196px;width:150px;height:60px;background:#1a1a1a}
.badge3{left:858px;width:200px;background:#d8dde8;border-radius:4px}

/* footer */
.footer-bg{left:0;top:2380px;width:1200px;height:456px}
.f-brand{left:230px;top:2474px;width:100px}
.f-brand .brand-mark{width:64px;height:64px}
.f-brand .brand-name{font-size:20px}
.f-phone{left:236px;top:2670px;font-size:13px;font-weight:600}
.f-col h4{font-size:15px;font-weight:600;text-transform:uppercase;margin-bottom:10px}
.f-links{list-style:none;font-size:12px;line-height:24px}
.f-links li::before{content:"› ";color:var(--blue)}
.f-company{left:446px;top:2500px}
.f-sub{left:676px;top:2500px}
.sub-row{display:flex;margin-bottom:26px}
.sub-input{width:210px;height:36px;border:1px solid var(--line);font-size:11px;color:var(--muted);padding:0 12px;line-height:34px;border-radius:18px 0 0 18px}
.sub-btn{width:104px;height:36px;line-height:36px;background:var(--blue);color:#fff;font-size:12px;font-weight:600;text-align:center;border-radius:0 18px 18px 0}
.socials{display:flex;gap:14px;margin-top:4px}
.socials span{width:40px;height:40px;border-radius:50%;background:var(--blue)}
.bottom-bar{left:0;top:2760px;width:1200px;height:76px;border-top:1px solid var(--line);background:#fff;font-size:12px;color:var(--ink)}
.copy{left:218px;top:28px}
.legal{left:840px;top:28px}
</style>
</head>
<body>
<div class="page">

  <!-- hero -->
  <div class="abs hero-photo" role="img" aria-label="Woman mopping the floor of a bright white bathroom"></div>
  <svg class="abs hero-curve" viewBox="0 0 1200 200" preserveAspectRatio="none">
    <path d="M0 70 C300 150 900 170 1200 70 L1200 200 L0 200 Z" fill="#ffffff"/>
    <path d="M0 70 C300 150 900 170 1200 70" fill="none" stroke="#2bb3ef" stroke-width="6"/>
  </svg>

  <header>
    <div class="abs brand">
      <div class="brand-mark"></div>
      <div class="brand-name">Dusk n Shine</div>
    </div>
    <div class="abs call">
      <svg width="26" height="26" viewBox="0 0 24 24"><path fill="#2b2b2b" d="M6.6 10.8a15.1 15.1 0 0 0 6.6 6.6l2.2-2.2c.3-.3.7-.4 1-.2 1.1.4 2.3.6 3.6.6.6 0 1 .4 1 1V20c0 .6-.4 1-1 1A17 17 0 0 1 3 4c0-.6.4-1 1-1h3.5c.6 0 1 .4 1 1 0 1.3.2 2.5.6 3.6.1.3 0 .7-.2 1z"/></svg>
      <div><small>Call us now</small><strong>0400 555 318</strong></div>
    </div>
    <span class="abs btn btn-quote">GET A QUOTE</span>
    <nav class="abs nav">
      <a class="active">HOME</a><a>ABOUT</a><a>CLEANINGS</a><a>PEST CONTROL</a><a>TIPS</a><a>CONTACT</a>
    </nav>
  </header>

  <h1 class="abs hero-title">Cleaning<br><span class="small">Service <span class="amp">&amp; Pest</span></span><br><span class="small amp">Controllers</span></h1>
  <span class="abs btn btn-book">Book A Service</span>

  <!-- services -->
  <div class="abs sq sq1"></div>
  <div class="abs sq sq2"></div>
  <h2 class="abs services-title">SERVICES <b>WE OFFERD</b></h2>

  <div class="abs card card-left">
    <div class="icon-circle"><svg width="40" height="40" viewBox="0 0 24 24"><path fill="#fff" d="M9 2h6v3h-2v3h3l2 4v10H6V12l2-4h3V5H9z"/></svg></div>
    <h3>Cleaning</h3>
    <p>Lorem Ipsum is simply dummy text of the printing and typesetting industry. Lorem Ipsum has been</p>
    <span class="btn-learn">LEARN MORE</span>
  </div>
  <div class="abs card card-mid" role="img" aria-label="Carpet being vacuumed">
    <div class="icon-circle"><svg width="40" height="40" viewBox="0 0 24 24"><path fill="none" stroke="#fff" stroke-width="1.6" d="M12 3v10M7 21l5-8 5 8zM4 21h16"/></svg></div>
    <h3>Carpet Cleaning</h3>
    <p>Lorem Ipsum is simply dummy text of the printing and typesetting industry. Lorem Ipsum has been</p>
    <span class="btn-learn">LEARN MORE</span>
  </div>
  <div class="abs card card-right">
    <div class="icon-circle"><svg width="40" height="40" viewBox="0 0 24 24"><path fill="#fff" d="M8 3h8v3h-2v2l4 3v10H6V11l4-3V6H8z"/></svg></div>
    <h3>Pest Control</h3>
    <p>Lorem Ipsum is simply dummy text of the printing and typesetting industry. Lorem Ipsum has been</p>
    <span class="btn-learn">LEARN MORE</span>
  </div>

  <!-- contact band -->
  <div class="abs band-photo" role="img" aria-label="Vacuum cleaner on a dark carpet"></div>
  <svg class="abs band" viewBox="0 0 1200 700" preserveAspectRatio="none">
    <path d="M0 0 L1200 0 L1200 40 C900 70 600 -10 0 70 Z" fill="#ffffff"/>
    <path d="M0 620 C300 700 700 540 1200 640 L1200 700 L0 700 Z" fill="#ffffff"/>
  </svg>
  <div class="abs email">info@dusknshine.com.au</div>
  <span class="abs btn btn-submit">Submit</span>
  <form class="abs form">
    <div class="field">First Name</div>
    <div class="field grey">Sur name</div>
    <div class="field grey">Email</div>
    <div class="field grey">Phone</div>
    <span class="btn-sign">Sign Up Now</span>
  </form>

  <!-- partners -->
  <div class="abs badge badge1"></div>
  <div class="abs badge badge2"></div>
  <div class="abs badge2b"></div>
  <div class="abs badge badge3"></div>

  <!-- footer -->
  <svg class="abs footer-bg" viewBox="0 0 1200 456" preserveAspectRatio="none">
    <path d="M0 60 C400 0 800 0 1200 60 L1200 456 L0 456 Z" fill="#f4f5f7"/>
  </svg>
  <div class="abs brand f-brand">
    <div class="brand-mark"></div>
    <div class="brand-name">Dusk n Shine</div>
  </div>
  <div class="abs f-phone">0400 555 318</div>
  <div class="abs f-col f-company">
    <h4>Company</h4>
    <ul class="f-links">
      <li>Products</li><li>About Us</li><li>Cleaning</li><li>Pet Control</li><li>Tips</li><li>Contact Us</li>
    </ul>
  </div>
  <div class="abs f-col f-sub">
    <h4>Subscribe</h4>
    <div class="sub-row"><div class="sub-input">Email address</div><div class="sub-btn">Subscribe</div></div>
    <h4>Follow Us</h4>
    <div class="socials"><span></span><span></span><span></span></div>
  </div>

  <div class="abs bottom-bar">
    <span class="abs copy">© 2021 dusknshine. All Rights Reserved.</span>
    <span class="abs legal">Privacy Policy &nbsp;|&nbsp; Terms of Use</span>
  </div>

</div>
</body>
</html>
```